Social Media Post Quote #4 - Native American Organization

- KINDLER - must be included
- Protect your community. Protect Your Elders. Stay Vaccinated. must be included
- Attached, company Logo, campaign logos and sample flu social media image. - our audience likes BRIGHT colors.
- Must include image from the United States, representing Land/Nature from one of the following regions, Plains and Woodlands, or Southwest, or Mountains, or Coast.
- must include quote: Our wisdom carries through generations.
- One image will be provided twice - incorporating campaign logos - in some fashion
Inspiration: https://torvelink.org/ and https://www.facebook.com/Torvelink

```html
<!DOCTYPE html>
<html lang="en">
<head>
<meta charset="utf-8">
<title>Kindler – Protect Your Elders</title>
<link rel="stylesheet" href="https://fonts.googleapis.com/css2?family=Barlow+Condensed:wght@400;500;700&family=Barlow+Semi+Condensed:wght@500&family=Cinzel:wght@600&display=swap">
<style>
  :root {
    --teal: #3a9aa1;
    --rust: #a4443d;
    --white: #ffffff;
    --paper: #f4f1ec;
    --glass: rgba(66, 82, 48, 0.72);
  }
  * { margin: 0; padding: 0; box-sizing: border-box; }
  html, body { width: 1200px; height: 1196px; overflow: hidden; background: var(--white); }
  .post { position: relative; width: 1200px; height: 1196px; overflow: hidden; }
  .frame-pattern {
    position: absolute; inset: 0;
    background: linear-gradient(135deg, #c98d87 0%, #9cc9cc 50%, #c98d87 100%);
  }
  .landscape {
    position: absolute; left: 34px; top: 34px; right: 34px; bottom: 34px;
    background:
      radial-gradient(ellipse 38% 45% at 50% 18%, rgba(236,232,222,0.95) 0%, rgba(210,206,190,0.6) 45%, rgba(0,0,0,0) 75%),
      linear-gradient(90deg, #2c3a22 0%, #4d5c36 18%, rgba(120,130,100,0.4) 40%, rgba(150,150,130,0.3) 60%, #55653a 82%, #2f3d24 100%),
      linear-gradient(180deg, #d9d8cf 0%, #8e9573 40%, #5a6445 62%, #585650 78%, #45423d 100%);
  }
  .campaign-badge {
    position: absolute; left: 78px; top: 90px; width: 414px; height: 120px;
    background: var(--paper); border: 4px solid var(--rust);
    text-align: center;
  }
  .campaign-name {
    display: block; margin-top: 6px;
    font: 700 74px/1 "Barlow Condensed", sans-serif; letter-spacing: 4px; color: var(--teal);
  }
  .campaign-sub {
    display: block; margin-top: 8px;
    font: 600 13px/1 "Cinzel", serif; letter-spacing: 0.5px; color: var(--rust);
  }
  .org-mark {
    position: absolute; left: 930px; top: 96px; width: 200px;
    display: flex; flex-direction: column; align-items: center; gap: 12px;
  }
  .org-square { width: 54px; height: 54px; background: var(--teal); }
  .org-name {
    font: 700 24px/1.05 "Barlow Condensed", sans-serif; color: var(--rust);
    text-align: center; text-transform: uppercase;
  }
  .steps { position: absolute; left: 0; top: 0; }
  .headline {
    position: absolute; left: 92px; top: 258px;
    font: 400 56px/65px "Barlow Condensed", sans-serif; color: var(--white);
    text-transform: uppercase;
  }
  .headline strong { font-weight: 700; }
  .quote-box {
    position: absolute; left: 237px; top: 573px; width: 723px; height: 372px;
    background: var(--glass); border: 2px solid rgba(255,255,255,0.85);
  }
  .quote-mark {
    position: absolute; left: 520px; top: 488px; width: 160px; text-align: center;
    font: 700 200px/1 "Barlow Condensed", sans-serif; color: var(--white);
  }
  .quote-text {
    position: absolute; left: 237px; top: 665px; width: 723px; text-align: center;
    font: 500 62px/66px "Barlow Semi Condensed", sans-serif; color: var(--white);
  }
</style>
</head>
<body>
<main class="post">
  <div class="frame-pattern" role="img" aria-label="Zigzag patterned border in teal and rust on white"></div>
  <div class="landscape" role="img" aria-label="Photograph of a misty road running through a tall coastal redwood forest"></div>

  <div class="campaign-badge">
    <span class="campaign-name">KINDLER</span>
    <span class="campaign-sub">COVID-19 &amp; FLU VACCINATION CAMPAIGN</span>
  </div>

  <div class="org-mark">
    <div class="org-square"></div>
    <div class="org-name">Torvelink Circle<br>for Native Elders</div>
  </div>

  <svg class="steps" width="1200" height="1196" viewBox="0 0 1200 1196" aria-hidden="true">
    <polyline points="90,468 535,468 535,408 672,408 672,342 745,342 745,278"
              fill="none" stroke="var(--teal)" stroke-width="7"/>
    <polygon points="78,255 728,255 728,322 655,322 655,387 518,387 518,452 78,452" fill="var(--rust)"/>
  </svg>

  <h1 class="headline">
    <strong>Protect</strong> your community.<br>
    <strong>Protect</strong> your elders.<br>
    <strong>Stay</strong> vaccinated.
  </h1>

  <div class="quote-box"></div>
  <div class="quote-mark">&ldquo;</div>
  <p class="quote-text">Our wisdom<br>carries through<br>generations.</p>
</main>
</body>
</html>
```